KTR Van Wrap for Printing Business

I need a fill wrap that is professional and sleek. I want it to stand out but not be so cluttered and full of stuff that it looks stupid. I uploaded 3 designs from the wrap guy that are childish and cartoonish. Really just took some existing stuff and threw it together. Looks stupid and phallic to me. I uploaded his 3 designs which are bad (1 being the best of them), my logo, Van template, actual photos of the van and a photo I grabbed on google of a Vornaplo Van which is simple and cool. I don't mind textures and backgrounds but I don't want it to look like a 10 year old made in in Canva.
I need my address and phone number on door as per the law for commercial vehicles.
As far as the rest of the van, phone number is not important, just the domain.
On my logo sheet are a few services we offer that I would like on the design.
Digital Printing and Wide Format Printing

```html
<!DOCTYPE html>
<html lang="en">
<head>
<meta charset="utf-8">
<title>Halbrook Print — Van Wrap Concepts</title>
<link rel="stylesheet" href="https://fonts.googleapis.com/css2?family=Montserrat:wght@600;800&family=Oswald:wght@500&display=swap">
<style>
  :root {
    --wrap-blue: #1f8ac4;
    --wrap-black: #141414;
    --ring-grey: #c6c6c6;
    --panel-light: #e4e4e4;
    --glass: #8d8d8d;
    --glass-dark: #5e5e5e;
    --tyre: #1a1a1a;
    --hub: #b9b9b9;
    --tail-red: #c22a2a;
    --signal-amber: #e88a1a;
    --ink-dark: #3f3f3f;
    --white: #ffffff;
    --page: #ffffff;
    --shadow: #0b0b0b;
  }
  html, body { margin: 0; padding: 0; width: 1200px; height: 1200px; overflow: hidden; background: var(--page); }
  .canvas { display: block; width: 1200px; height: 1200px; }
  .brand-name { font-family: "Montserrat", sans-serif; font-weight: 800; fill: var(--wrap-blue); }
  .brand-phone { font-family: "Montserrat", sans-serif; font-weight: 600; letter-spacing: 2.5px; }
  .brand-web { font-family: "Montserrat", sans-serif; font-weight: 800; fill: var(--wrap-blue); font-size: 8.5px; letter-spacing: .5px; }
  .service { font-family: "Oswald", sans-serif; font-weight: 500; fill: var(--white); font-size: 12.5px; }
  .emblem-name { font-family: "Montserrat", sans-serif; font-weight: 800; }
  .social-name { font-family: "Oswald", sans-serif; font-weight: 500; fill: var(--white); font-size: 8px; }
</style>
</head>
<body>
<svg class="canvas" viewBox="0 0 970 970" xmlns="http://www.w3.org/2000/svg">
  <defs>
    <path id="van-body" d="M48,165 Q50,100 105,96 L630,96 Q680,98 720,130 L790,205 Q860,220 900,240 Q925,255 925,300 L925,338 L822,345 A55,55 0 0 0 716,345 L290,348 A58,58 0 0 0 176,348 L60,350 Q45,346 45,320 Z"/>
    <clipPath id="van-clip"><use href="#van-body"/></clipPath>
    <g id="van-chassis">
      <ellipse cx="480" cy="405" rx="440" ry="22" fill="var(--shadow)"/>
      <rect x="42" y="315" width="40" height="38" rx="4" fill="var(--wrap-black)"/>
      <circle cx="232" cy="370" r="50" fill="var(--tyre)"/>
      <circle cx="232" cy="370" r="29" fill="var(--hub)"/>
      <circle cx="232" cy="370" r="9" fill="var(--ink-dark)"/>
      <circle cx="769" cy="368" r="50" fill="var(--tyre)"/>
      <circle cx="769" cy="368" r="29" fill="var(--hub)"/>
      <circle cx="769" cy="368" r="9" fill="var(--ink-dark)"/>
    </g>
    <g id="van-details">
      <path d="M572,120 L658,120 L664,206 L572,206 Z" fill="var(--glass)"/>
      <path d="M668,118 L700,122 L786,206 L676,206 Z" fill="var(--glass-dark)"/>
      <rect x="64" y="160" width="13" height="40" rx="3" fill="var(--tail-red)"/>
      <path d="M870,255 L906,255 L908,305 L870,305 Z" fill="var(--wrap-black)"/>
      <rect x="876" y="291" width="30" height="10" fill="var(--signal-amber)"/>
      <path d="M835,312 L926,308 L926,340 L835,344 Z" fill="var(--wrap-black)"/>
      <line x1="806" y1="205" x2="804" y2="92" stroke="var(--hub)" stroke-width="1.5"/>
      <g class="social">
        <circle cx="776" cy="253" r="9" fill="var(--white)" fill-opacity=".25"/>
        <text class="social-name" x="776" y="256" text-anchor="middle">Linkly</text>
        <circle cx="806" cy="253" r="9" fill="var(--white)" fill-opacity=".25"/>
        <text class="social-name" x="806" y="256" text-anchor="middle">Photon</text>
      </g>
      <g class="services">
        <circle cx="583" cy="255" r="2.5" fill="var(--white)"/><text class="service" x="589" y="260">DIGITAL PRINTING</text>
        <circle cx="583" cy="275" r="2.5" fill="var(--white)"/><text class="service" x="589" y="280">LARGE FORMAT PRINTING</text>
        <circle cx="583" cy="295" r="2.5" fill="var(--white)"/><text class="service" x="589" y="300">DIRECT MAIL</text>
        <circle cx="583" cy="315" r="2.5" fill="var(--white)"/><text class="service" x="589" y="320">CUSTOM FINISHING</text>
      </g>
      <text class="brand-name" x="210" y="160" text-anchor="middle" font-size="27">HALBROOK</text>
      <text class="brand-name" x="210" y="191" text-anchor="middle" font-size="27">PRINT</text>
      <text class="brand-web" x="202" y="259" text-anchor="middle">WWW.HALBROOKPRINT.COM</text>
    </g>
  </defs>

  <g class="van van--blue-emblem">
    <use href="#van-chassis"/>
    <g clip-path="url(#van-clip)">
      <rect x="0" y="80" width="430" height="300" fill="var(--wrap-black)"/>
      <rect x="430" y="80" width="520" height="300" fill="var(--wrap-blue)"/>
      <rect x="60" y="210" width="380" height="11" fill="var(--wrap-blue)"/>
      <rect x="60" y="236" width="260" height="5" fill="var(--wrap-blue)"/>
      <circle cx="440" cy="228" r="112" fill="var(--wrap-blue)" stroke="var(--ring-grey)" stroke-width="10"/>
      <text class="emblem-name" x="440" y="222" text-anchor="middle" font-size="30" fill="var(--white)">HALBROOK</text>
      <text class="emblem-name" x="440" y="256" text-anchor="middle" font-size="30" fill="var(--white)">PRINT</text>
    </g>
    <use href="#van-details"/>
    <text class="brand-phone" x="202" y="236" text-anchor="middle" font-size="19" fill="var(--white)">201.555.0148</text>
  </g>

  <g class="van van--light-emblem" transform="translate(0,450)">
    <use href="#van-chassis"/>
    <g clip-path="url(#van-clip)">
      <rect x="0" y="80" width="430" height="300" fill="var(--wrap-black)"/>
      <rect x="430" y="80" width="520" height="300" fill="var(--wrap-blue)"/>
      <rect x="60" y="215" width="380" height="26" fill="var(--panel-light)"/>
      <circle cx="440" cy="228" r="112" fill="var(--panel-light)" stroke="var(--ring-grey)" stroke-width="10"/>
      <text class="emblem-name" x="440" y="222" text-anchor="middle" font-size="30" fill="var(--ink-dark)">HALBROOK</text>
      <text class="emblem-name" x="440" y="256" text-anchor="middle" font-size="30" fill="var(--ink-dark)">PRINT</text>
    </g>
    <use href="#van-details"/>
    <text class="brand-phone" x="202" y="235" text-anchor="middle" font-size="19" fill="var(--wrap-black)">201.555.0148</text>
  </g>
</svg>
</body>
</html>
```